TealFathom.com Website design needed!!

We are looking for a website layout to match the attached logo. We specialize in Dive Charters and currently are located in the Virgin Islands off of St. Thomas. Please create a design that is compatible with Bootstrap and have the grid in mind. WE are looking for creative and extremely professional layout design.

Target Market(s)

Scuba Diving, Divers looking for a diving charter in the Virgin Islands.

Number of Pages Required

3 page

Font styles to use
Serif

Requirements
Must have
• Must be Bootstrap friendly.
• Must work with the logo we provided. Colors etc.

```html
<!DOCTYPE html>
<html lang="en">
<head>
<meta charset="utf-8">
<title>Teal Fathom – Diving Charters and Scuba</title>
<link href="https://fonts.googleapis.com/css2?family=PT+Sans:wght@400;700&family=PT+Serif:wght@400;700&display=swap" rel="stylesheet">
<style>
:root{
  --navy:#0e2238;
  --ink:#1b1b1b;
  --text:#6b6b6b;
  --blue:#1a8fe8;
  --red:#d3282f;
  --light:#f3f3f3;
  --white:#ffffff;
  --ring:#d6d6d6;
}
*{margin:0;padding:0;box-sizing:border-box}
html,body{width:1200px;height:3593px;overflow:hidden}
body{position:relative;background:var(--white);font-family:"PT Serif",Georgia,serif;color:var(--text)}
.abs{position:absolute}
h1,h2,h3,h4,.nav a,.btn,.sans{font-family:"PT Sans",Arial,sans-serif}
.btn{position:absolute;display:flex;align-items:center;justify-content:center;color:#fff;font-size:11px;font-weight:700;text-transform:uppercase;background:var(--red);width:137px;height:39px;text-decoration:none}
.btn.dark{background:#000}
.btn.blue{background:var(--blue)}

/* hero */
.hero{position:absolute;left:0;top:0;width:1200px;height:608px;background:linear-gradient(160deg,#1c7fb4 0%,#2a9fcf 40%,#11618f 75%,#0b3c5e 100%)}
.nav{position:absolute;left:0;top:0;width:1200px;height:77px;background:rgba(20,24,30,.88)}
.nav a{position:absolute;top:0;height:77px;display:flex;align-items:center;justify-content:center;color:#fff;font-size:12px;font-weight:700;text-decoration:none;text-transform:uppercase}
.nav a.active{background:var(--blue)}
.brand{position:absolute;left:96px;top:72px;width:232px;height:196px;background:#1d1f24;display:flex;align-items:center;justify-content:center;gap:10px;color:#fff;font-family:"PT Sans",Arial,sans-serif;font-weight:700;font-size:28px}
.brand i{width:16px;height:16px;border-radius:50%;background:var(--red);display:block}
.hero h1{position:absolute;left:98px;top:288px;color:#fff;font-size:54px;line-height:62px;font-weight:700;text-transform:uppercase}
.search{position:absolute;left:697px;top:125px;width:400px;height:407px;background:var(--blue)}
.search .top{height:179px;background:rgba(30,32,38,.92);padding:22px 26px;color:#fff}
.search h3{font-size:21px;line-height:24px;text-transform:uppercase}
.search h3 span{color:var(--blue)}
.search label{display:flex;align-items:center;gap:18px;font-size:13px;margin-top:16px;font-family:"PT Sans",Arial,sans-serif}
.search label b{width:14px;height:14px;border-radius:50%;background:#fff;display:block}
.field{position:absolute;left:28px;width:344px;height:38px;background:#fff;font-size:11px;color:#aaa;padding:12px 14px;font-family:"PT Sans",Arial,sans-serif}
.field.muted{background:#e6e6e6}
.search .go{position:absolute;left:28px;top:346px;width:344px;height:42px;background:#000;color:#fff;font-size:11px;display:flex;align-items:center;justify-content:center;font-family:"PT Sans",Arial,sans-serif;text-transform:uppercase}
.dots{position:absolute;display:flex;gap:6px}
.dots b{width:11px;height:11px;border-radius:50%;background:#fff;display:block}
.dots b.on{background:#222}

/* welcome */
.welcome{position:absolute;top:608px;left:0;width:1200px;height:522px;background:var(--light)}
.welcome h2{position:absolute;left:100px;top:40px;font-size:26px;color:var(--ink);text-transform:uppercase}
.rule{position:absolute;left:100px;top:104px;width:998px;height:2px;background:#c9d9ea}
.rule b{position:absolute;left:0;top:-4px;width:96px;height:9px;background:var(--blue);display:block}
.photo{position:absolute}
.welcome h3{position:absolute;left:618px;top:152px;font-size:26px;color:var(--ink);text-transform:uppercase}
.welcome p{position:absolute;left:618px;width:480px;font-size:13px;line-height:22px}

/* schedule */
.schedule{position:absolute;top:1130px;left:0;width:1200px;height:508px;background:linear-gradient(180deg,#0f2a44 0%,#112f4c 60%,#0b2238 100%)}
.schedule h2,.services h2,.news h2,.reviews h2{position:absolute;left:0;width:1200px;text-align:center;font-size:36px;text-transform:uppercase}
.schedule h2{top:42px;color:#fff}
.count{position:absolute;top:110px;text-align:center;width:72px}
.count small{display:block;color:#fff;font-size:10px;font-family:"PT Sans",Arial,sans-serif;margin-bottom:8px}
.count b{display:block;height:76px;background:#1e1f22;color:#fff;font-size:52px;line-height:76px;font-family:"PT Sans",Arial,sans-serif}
.count b.hot{background:#b8161c}
.slot{position:absolute;top:288px;width:206px;color:#fff}
.slot h3{font-size:23px;padding-bottom:10px;border-bottom:1px solid rgba(255,255,255,.5)}
.slot p{font-size:13px;line-height:20px;margin-top:10px;font-family:"PT Sans",Arial,sans-serif}
.slot a{position:absolute;top:149px;left:0;color:#fff;font-size:10px;font-weight:700;text-decoration:none;font-family:"PT Sans",Arial,sans-serif}
.slot a.red{color:var(--red)}

/* services */
.services{position:absolute;top:1638px;left:0;width:1200px;height:542px;background:#fff}
.services h2{top:42px;color:var(--ink)}
.service{position:absolute;top:120px;width:230px;text-align:center}
.service-badge{width:134px;height:134px;margin:0 auto;border-radius:50%;border:10px solid var(--ring)}
.service h3{color:var(--red);font-size:26px;margin-top:30px;font-weight:400}
.service p{font-size:13px;line-height:18px;margin:8px auto 0;width:190px;color:#555}

/* news */
.news{position:absolute;top:2180px;left:0;width:1200px;height:558px;background:linear-gradient(180deg,#2f6f64 0%,#2aa8b0 45%,#4fd0d4 75%,#8fd8dc 100%)}
.news h2{top:40px;color:#fff}
.card{position:absolute;top:124px;width:228px;height:369px;background:#fff;text-align:center}
.card.dark{background:#141414}
.card .pic{position:absolute;left:14px;top:14px;width:200px;height:150px}
.card h4{position:absolute;left:14px;top:188px;width:200px;font-size:16px;line-height:22px;color:var(--ink);text-transform:uppercase}
.card.dark h4,.card.dark p{color:#fff}
.card p{position:absolute;left:22px;top:246px;width:184px;font-size:13px;line-height:18px;color:#333}
.card .btn{left:46px;top:310px}
.arrow{position:absolute;top:2456px;width:54px;height:54px;background:rgba(40,40,40,.85)}

/* reviews */
.reviews{position:absolute;top:2738px;left:0;width:1200px;height:376px;background:#fff}
.reviews h2{top:38px;color:var(--ink)}
.reviews .name{position:absolute;top:212px;left:0;width:1200px;text-align:center;font-size:14px;font-weight:700;font-style:italic;color:var(--ink)}
.reviews blockquote{position:absolute;top:252px;left:170px;width:860px;text-align:center;font-size:13px;line-height:20px;color:#333}
.quote{position:absolute;font-size:50px;font-family:"PT Serif",Georgia,serif;color:#222;line-height:1}

/* footer */
.footer{position:absolute;top:3114px;left:0;width:1200px;height:479px;background:linear-gradient(180deg,#11355a 0%,#0f2f52 60%,#0b2440 100%);color:#fff}
.footer h4{position:absolute;top:50px;font-size:24px}
.col{position:absolute;top:118px;font-size:11px;line-height:22px;font-family:"PT Sans",Arial,sans-serif}
.links{list-style:none;width:230px}
.links li{border-bottom:1px solid rgba(255,255,255,.6);padding:4px 0 6px;line-height:22px}
.tweets p{width:230px;margin-bottom:14px;line-height:20px}
.input{position:absolute;left:874px;width:228px;height:36px;background:#fff;color:#aaa;font-size:11px;padding:10px 12px;font-family:"PT Sans",Arial,sans-serif}
.submit{position:absolute;left:874px;width:96px;height:30px;background:var(--blue);font-size:11px;font-weight:700;display:flex;align-items:center;justify-content:center;font-family:"PT Sans",Arial,sans-serif}
.copy{position:absolute;left:98px;top:438px;font-size:11px;font-family:"PT Sans",Arial,sans-serif}
</style>
</head>
<body>

<header class="hero" role="img" aria-label="Underwater photo of a diver in a mask swimming near the surface">
  <nav class="nav">
    <a class="active" href="#" style="left:421px;width:135px">Teal Fathom</a>
    <a href="#" style="left:556px;width:114px">About us</a>
    <a href="#" style="left:670px;width:101px">Contact</a>
    <a href="#" style="left:771px;width:129px">Learn more</a>
    <a href="#" style="left:900px;width:111px">Schedule</a>
  </nav>
  <div class="brand"><i></i>Teal Fathom</div>
  <h1>Teal Fathom<br>Charters<br>and Scuba</h1>
  <form class="search">
    <div class="top">
      <h3>Search for your dream<br>charter <span>today!</span></h3>
      <label><b></b>I have approximate dates</label>
      <label><b></b>I’m flexible</label>
    </div>
    <div class="field muted" style="top:204px">FIRST NAME</div>
    <div class="field" style="top:260px">EMAIL</div>
    <div class="go">Find charters</div>
  </form>
  <div class="dots" style="left:558px;top:554px"><b></b><b></b><b class="on"></b><b></b><b></b></div>
</header>

<section class="welcome">
  <h2>Welcome to Teal Fathom Charters and Scuba</h2>
  <div class="rule"><b></b></div>
  <div class="photo" role="img" aria-label="Photo of a diver in a mask underwater" style="left:100px;top:154px;width:480px;height:321px;background:linear-gradient(160deg,#3fb3e0,#1478b0 55%,#0b4b78)"></div>
  <h3>Who we are?</h3>
  <p style="top:196px">Vut sagittis a, magna ridiculus! Scelerisque parturient! Cum duis nunc in, dignissim, purus porta enim, proin turpis egestas! Mauris dapibus sed integer placerat, scelerisque! Ac enim nascetur rhoncus facilisis phasellus eu sit turpis purus magna auctor nunc facilisis parturient ac tempor, montes etiam tortor rhoncus! In, aliquam. Elementum urna, tincidunt? Nisi ut urna? Arcu, odio facilisis urna magna vel, elementum integer quis nisi scelerisque etiam.</p>
  <p style="top:340px">purus magna auctor nunc facilisis parturient ac tempor, montes etiam tortor rhoncus! In, aliquam. Elementum urna, tincidunt? Nisi ut urna? Arcu, odio facilisis urna magna vel, elementum integer quis nisi scelerisque etiam.</p>
  <a class="btn" href="#" style="left:616px;top:436px">Read more</a>
</section>

<section class="schedule" aria-label="Our schedule">
  <h2>Our Schedule</h2>
  <div class="count" style="left:410px"><small>DAYS</small><b class="hot">32</b></div>
  <div class="count" style="left:512px"><small>HOURS</small><b>17</b></div>
  <div class="count" style="left:613px"><small>MINUTES</small><b>04</b></div>
  <div class="count" style="left:714px"><small>SECONDS</small><b>59</b></div>
  <div class="slot" style="left:98px"><h3>Schedule 01</h3><p>Date: 20 February, 2016<br>Place: Virgin Island<br>Timimng: 8:00am - 4:00pm</p><a href="#">READ MORE</a></div>
  <div class="slot" style="left:354px"><h3>Schedule 02</h3><p>Date: 23 February, 2016<br>Place: Virgin Island<br>Timimng: 8:00am - 4:00pm</p><a class="red" href="#">READ MORE</a></div>
  <div class="slot" style="left:613px"><h3>Schedule 03</h3><p>Date: 26 February, 2016<br>Place: Virgin Island<br>Timimng: 8:00am - 4:00pm</p><a href="#">READ MORE</a></div>
  <div class="slot" style="left:869px"><h3>Schedule 03</h3><p>Date: 29 February, 2016<br>Place: Virgin Island<br>Timimng: 8:00am - 4:00pm</p><a href="#">READ MORE</a></div>
</section>

<section class="services">
  <h2>Our Diving Services</h2>
  <div class="service" style="left:105px">
    <div class="service-badge" role="img" aria-label="Service illustration: messaging" style="background:#34495e"></div>
    <h3>Service 01</h3><p>Lorem ipsum dolor sit amet, consectetur adipiscing elit. Fusce semper vitae leo sit amet vehicula.</p>
  </div>
  <div class="service" style="left:357px">
    <div class="service-badge" role="img" aria-label="Service illustration: instructor" style="background:#e05a3c"></div>
    <h3>Service 01</h3><p>Lorem ipsum dolor sit amet, consectetur adipiscing elit. Fusce semper vitae leo sit amet vehicula.</p>
  </div>
  <div class="service" style="left:608px">
    <div class="service-badge" role="img" aria-label="Service illustration: training presentation" style="background:#f1c40f"></div>
    <h3>Service 01</h3><p>Lorem ipsum dolor sit amet, consectetur adipiscing elit. Fusce semper vitae leo sit amet vehicula.</p>
  </div>
  <div class="service" style="left:869px">
    <div class="service-badge" role="img" aria-label="Service illustration: online booking" style="background:#1abc9c"></div>
    <h3>Service 01</h3><p>Lorem ipsum dolor sit amet, consectetur adipiscing elit. Fusce semper vitae leo sit amet vehicula.</p>
  </div>
  <a class="btn" href="#" style="left:151px;top:450px">Read more</a>
  <a class="btn" href="#" style="left:403px;top:450px">Read more</a>
  <a class="btn dark" href="#" style="left:661px;top:450px">Read more</a>
  <a class="btn" href="#" style="left:919px;top:450px">Read more</a>
</section>

<section class="news" role="img" aria-label="Tropical lagoon with overwater bungalows and turquoise water">
  <h2>Latest News</h2>
  <article class="card" style="left:72px"><div class="pic" role="img" aria-label="Photo of a diver underwater" style="background:linear-gradient(160deg,#4aa3c8,#1d5f86)"></div><h4>This is a test<br>title</h4><p>This is my test Body. Her is a link to our Special.</p><a class="btn" href="#">Read more</a></article>
  <article class="card" style="left:328px"><div class="pic" role="img" aria-label="Photo of a coral reef with fish" style="background:linear-gradient(160deg,#3f9fd6,#1a6aa8 60%,#d36f3a)"></div><h4>Caribbean luxury<br>yacht charter</h4><p>A Caribbean luxury yacht charter is the most exclusive</p><a class="btn" href="#">Read more</a></article>
  <article class="card dark" style="left:584px"><div class="pic" role="img" aria-label="Photo of a diver in open blue water" style="background:linear-gradient(160deg,#2c9fe0,#0d5a9a)"></div><h4>This is a test<br>title</h4><p>This is my test Body. Her is a link to our Special.</p><a class="btn blue" href="#">Read more</a></article>
  <article class="card" style="left:843px"><div class="pic" role="img" aria-label="Photo of a snorkeller near the surface" style="background:linear-gradient(160deg,#5ec3ea,#1f86c0)"></div><h4>Caribbean luxury<br>yacht charter</h4><p>A Caribbean luxury yacht charter is the most exclusive</p><a class="btn" href="#">Read more</a></article>
</section>
<svg class="arrow" style="left:72px" viewBox="0 0 54 54" aria-hidden="true"><path d="M32 16L21 27l11 11" stroke="#fff" stroke-width="4" fill="none"/></svg>
<svg class="arrow" style="left:1016px" viewBox="0 0 54 54" aria-hidden="true"><path d="M22 16l11 11-11 11" stroke="#fff" stroke-width="4" fill="none"/></svg>

<section class="reviews">
  <h2>What People Say About Us</h2>
  <div class="abs" role="img" aria-label="Portrait of a customer in diving gear" style="left:550px;top:106px;width:100px;height:100px;border-radius:50%;background:linear-gradient(160deg,#2e9fd0,#0f5c86)"></div>
  <div class="name sans">Marla Quint</div>
  <span class="quote" style="left:138px;top:250px">“</span>
  <blockquote>Lorem ipsum dolor sit amet, consectetur adipiscing elit. Fusce semper vitae leo sit amet vehicula. Sed viverra, justo ac consectetur hendrerit, lacus elit tempor urna, gravida mattis lacus ex sed sem. Nam consectetur, arcu in iaculis dapibus</blockquote>
  <span class="quote" style="left:1034px;top:262px">”</span>
  <div class="dots" style="left:575px;top:328px"><b style="background:#aaa"></b><b style="background:var(--blue)"></b><b style="background:#aaa"></b></div>
</section>

<footer class="footer" role="img" aria-label="Divers swimming over a reef in deep blue water">
  <h4 style="left:98px">Contact</h4>
  <h4 style="left:357px">Quick Links</h4>
  <h4 style="left:613px">Latest Tweets</h4>
  <h4 style="left:874px">Contact Us</h4>
  <div class="col" style="left:98px;width:220px">
    TEAL FATHOM<br><br>(Harbour Office / Head Office)<br>Level 4, Suite 12 / 88 Harbour Lane,<br>Coral Bay, CB 2040<br>Phone: (05) 5550 142<br>(Reef Office)<br>Shop 3/210 Reef Road,<br>Palm Cove, PC 5120<br>(05) 5550 378
  </div>
  <ul class="col links" style="left:357px;top:112px">
    <li>+ Lorem ipsum dolor sit</li><li>+ Amet consectetur</li><li>+ Praesent vel sem id</li><li>+ Curabitur hendrerit est</li><li>+ Aliquam eget erat nec sapien</li><li>+ Cras id augue nunc</li><li>+ Sed a nulla urna</li>
  </ul>
  <div class="col tweets" style="left:613px">
    <p>@namehere Iusto nonummy laoreet phasellus posuere in amet integer pellus elit eget tincidunt. Nequatur laoreet justo a non tellus laoreet vitae dolore 1 day ago</p>
    <p>@namehere Iusto nonummy laoreet phasellus posuere in amet integer pellus elit eget tincidunt. Nequatur laoreet justo a non tellus laoreet vitae dolore 1 day ago</p>
  </div>
  <div class="input" style="top:120px">Full Name</div>
  <div class="input" style="top:168px">Email Address</div>
  <div class="input" style="top:212px">Subject</div>
  <div class="input" style="top:242px;height:80px;top:256px">Message</div>
  <div class="submit" style="top:350px">SUBMIT</div>
  <div class="copy">Copyright © 2016 TEAL FATHOM - All Rights Reserved</div>
</footer>

</body>
</html>
```